Business Card design for amazing new Dental Office

Please read this brief closely!

Our client is a modern new dental office/
They love their new logo.
Now it's time to create a business card for them.

It should be a two sided card:
Side one should have the logo and name and maybe a color background or design.
Side two should have all the contact information which is here:

Adrian Pellman, D.D.S
General and Cosmetic Dentistry
4187 W. Pinecrest Avenue
Ventura, CA 93011
(805) 912-4386
dradrian@bluefernsmiles-example.com
www.bluefernsmiles-example.com

Feel free to arrange that info as you like and to style both sides of the card according to your creativity. This is a chance for you to show your design skills!

Client is open to font choices and is looking for a style that is amazing and premium. Colors can be selected from the logo, or any variation of those.

You will not win this contest with a less than beautiful card design so please feel free to make multiple submissions.

Logo files attached and please message me with any questions.
Thanks!

Target Market(s)

Families and Professionals seeking dental services

Industry/Entity Type

Dental

Contact Information for Business Card

Logo, style, contact info as per the brief

Font styles to use
Sans Serif

Requirements
Must have
• Client's logo and contact details as per brief
Nice to have
• Unique style reflecting high end dental clinic near the beach
Should not have
• Must not look like a template

```html
<!DOCTYPE html>
<html lang="en">
<head>
<meta charset="utf-8">
<title>Blue Fern Smiles – Business Card</title>
<link rel="stylesheet" href="https://fonts.googleapis.com/css2?family=Josefin+Sans:wght@400;600&family=Roboto:wght@700&display=swap">
<style>
  :root {
    --backdrop: #8c8c8c;
    --card: #2d2d2e;
    --edge: #d6c52e;
    --name-blue: #3cb1ec;
    --accent-gold: #d9c03c;
    --text-light: #e6e6e6;
    --brand-grey: #c9c9c9;
    --divider: #9a9a9a;
  }
  * { box-sizing: border-box; margin: 0; padding: 0; }
  html, body {
    width: 1200px; height: 800px; overflow: hidden;
    background: var(--backdrop);
  }
  .canvas {
    width: 1200px; height: 800px;
    display: flex; align-items: center; justify-content: center; gap: 40px;
  }
  .card {
    position: relative;
    width: 550px; height: 314px;
    background: var(--card);
    border: 2px solid var(--edge);
    box-shadow: 0 14px 30px rgba(0,0,0,.35);
  }
  /* Contact side */
  .card--contact { display: flex; align-items: center; padding-bottom: 20px; }
  .identity {
    width: 232px; text-align: right; padding-right: 14px;
  }
  .identity__name {
    font-family: "Roboto", sans-serif; font-weight: 700;
    color: var(--name-blue); font-size: 19px; letter-spacing: .2px;
    white-space: nowrap;
  }
  .identity__name small { font-size: 12px; }
  .identity__role {
    font-family: "Josefin Sans", sans-serif; font-weight: 400;
    color: var(--accent-gold); font-size: 13.5px; margin-top: 5px;
    white-space: nowrap;
  }
  .divider { width: 1px; height: 100px; background: var(--divider); flex: none; }
  .contact {
    padding-left: 14px;
    font-family: "Josefin Sans", sans-serif; font-weight: 400;
    color: var(--text-light); font-size: 12px; line-height: 1.45;
    white-space: nowrap;
  }
  .contact__address { margin-bottom: 10px; }
  .contact__line { display: flex; align-items: center; gap: 6px; }
  .contact__icon { width: 10px; height: 10px; flex: none; }
  /* Brand side */
  .card--brand {
    display: flex; flex-direction: column; align-items: center; justify-content: center; gap: 18px;
    padding-top: 20px;
  }
  .brand__dot {
    width: 18px; height: 18px; border-radius: 50%; background: var(--accent-gold);
  }
  .brand__name {
    font-family: "Josefin Sans", sans-serif; font-weight: 400;
    color: var(--brand-grey); font-size: 30px; letter-spacing: 5px;
    text-transform: uppercase; white-space: nowrap;
  }
</style>
</head>
<body>
<main class="canvas">
  <section class="card card--contact" aria-label="Contact side">
    <div class="identity">
      <p class="identity__name">Adrian Pellman, <small>D.D.S</small></p>
      <p class="identity__role">General &amp; Cosmetic Dentistry</p>
    </div>
    <div class="divider"></div>
    <div class="contact">
      <p class="contact__address">4187 W. Pinecrest Avenue<br>Ventura, CA 93011</p>
      <p class="contact__line">
        <svg class="contact__icon" viewBox="0 0 10 10"><path d="M2 1 L4 1 L4.6 3 L3.4 3.8 Q4.4 5.8 6.2 6.6 L7 5.4 L9 6 L9 8 Q8.5 9 7.5 9 Q1 8 1 2.5 Q1 1.5 2 1 Z" fill="var(--accent-gold)"/></svg>
        (805) 912-4386
      </p>
      <p class="contact__line">
        <svg class="contact__icon" viewBox="0 0 10 10"><rect x="0.5" y="2" width="9" height="6.5" fill="var(--accent-gold)"/><path d="M0.5 2 L5 5.8 L9.5 2" fill="none" stroke="var(--card)" stroke-width="0.9"/></svg>
        dradrian@bluefernsmiles-example.com
      </p>
      <p class="contact__line">
        <svg class="contact__icon" viewBox="0 0 10 10"><circle cx="5" cy="5" r="4.5" fill="var(--accent-gold)"/><path d="M0.5 5 H9.5 M5 0.5 Q2.5 5 5 9.5 M5 0.5 Q7.5 5 5 9.5" fill="none" stroke="var(--card)" stroke-width="0.7"/></svg>
        www.bluefernsmiles-example.com
      </p>
    </div>
  </section>

  <section class="card card--brand" aria-label="Brand side">
    <span class="brand__dot"></span>
    <p class="brand__name">Blue Fern Smiles</p>
  </section>
</main>
</body>
</html>
```